make it look old timey and motherly but mordern...bath soak with cooling vapors. tall pine hush

need a bath soak label...cooling vapors. will be in a pouch like below. dont pay attention to the design, just attatching so you know the kind of pouch itll be in. need something trusty, minimal and clean...its called tall pine hush bath soak the best bath yull ever take.... for sore muscles, cooling vapors, smells good...made with menthol lemon and eucalyptus...give me something good.

Target Market(s)

make it look old timey and motherly but mordern

Font styles to use
Serif
Sans Serif

Colors
0054AA
0677BA
7BADD7
CADEEF
E8F1F8
0094D4
00A9DD
6FCCEA
C7EBF8
E9F6FB
FFF300
FFF600
FEFA6F
FFFEC7
FFFEE8
FFC000
F8CF3A
FAE287
FDF2CF
FEFAEE
E54698
E96AAD
F1A4CE
F9D9EA
FCEFF6
6B429C
8869AF
B7A5CE
E3DAEB
F3F0F8

```html
<!DOCTYPE html>
<html lang="en">
<head>
<meta charset="UTF-8">
<title>Tall Pine Hush Bath Soak – Cooling Vapors</title>
<link href="https://fonts.googleapis.com/css2?family=Marcellus&family=Alegreya+Sans:wght@400;500&display=swap" rel="stylesheet">
<style>
  :root {
    --canvas: #d0d0d0;
    --slate: #66767e;
    --slate-deep: #4e5d65;
    --slate-soft: #8a9aa1;
    --text-light: #f4f7f8;
    --text-grey: #76848a;
    --wash-blue: #b8d8e2;
    --wash-mint: #c9e6dc;
    --wash-white: #f3f8f9;
    --wash-aqua: #a9d3d6;
  }
  * { margin: 0; padding: 0; box-sizing: border-box; }
  html, body { width: 1200px; height: 800px; overflow: hidden; }
  body {
    background: var(--canvas);
    font-family: "Alegreya Sans", sans-serif;
    position: relative;
  }
  .label {
    position: absolute;
    left: 380px; top: 60px;
    width: 440px; height: 680px;
    overflow: hidden;
  }
  .label__wash {
    position: absolute; inset: 0;
    background:
      radial-gradient(ellipse at 20% 15%, var(--wash-blue) 0%, transparent 55%),
      radial-gradient(ellipse at 80% 55%, var(--wash-mint) 0%, transparent 50%),
      radial-gradient(ellipse at 85% 10%, var(--wash-aqua) 0%, transparent 45%),
      radial-gradient(ellipse at 25% 75%, var(--wash-white) 0%, transparent 60%),
      linear-gradient(160deg, var(--wash-blue), var(--wash-white) 45%, var(--wash-mint) 75%, var(--wash-blue));
  }
  .flavor-tab {
    position: absolute;
    left: 142px; top: 0;
    width: 152px; height: 137px;
    background: var(--slate);
    color: var(--text-light);
    font-family: "Marcellus", serif;
    font-size: 33px;
    line-height: 41px;
    text-align: center;
    padding-top: 28px;
    letter-spacing: 0.5px;
  }
  .brand-name {
    position: absolute;
    left: 0; right: 0; top: 212px;
    text-align: center;
    font-family: "Marcellus", serif;
    font-size: 24px;
    color: var(--text-grey);
    letter-spacing: 0.5px;
  }
  .product-frame {
    position: absolute;
    left: 87px; top: 251px;
    width: 264px; height: 57px;
    border: 2px solid var(--slate);
    text-align: center;
    font-family: "Marcellus", serif;
    font-size: 44px;
    line-height: 53px;
    color: var(--slate-deep);
  }
  .tagline-band {
    position: absolute;
    left: 28px; right: 30px; top: 382px;
    height: 25px;
    background: linear-gradient(90deg, var(--slate-soft), var(--slate-deep));
    color: var(--text-light);
    text-align: center;
    font-size: 21px;
    line-height: 25px;
    letter-spacing: 0.5px;
  }
  .benefits {
    position: absolute;
    left: 0; right: 0; top: 440px;
    list-style: none;
    text-align: center;
    color: var(--text-grey);
    font-size: 17px;
    line-height: 30px;
    letter-spacing: 0.3px;
  }
  .ingredients-pill {
    position: absolute;
    left: 125px; top: 555px;
    width: 190px; height: 36px;
    border-radius: 6px;
    background: linear-gradient(90deg, var(--slate-deep), var(--slate-soft));
    color: var(--text-light);
    text-align: center;
    font-size: 12.5px;
    line-height: 15px;
    padding-top: 3px;
  }
  .net-weight {
    position: absolute;
    left: 0; right: 0; top: 626px;
    text-align: center;
    color: var(--slate-deep);
    font-size: 13px;
    line-height: 18px;
  }
</style>
</head>
<body>
  <section class="label">
    <div class="label__wash" role="img" aria-label="Soft blue, mint and white watercolor marble backdrop"></div>
    <div class="flavor-tab">COOLING<br>VAPORS</div>
    <p class="brand-name">TALL PINE HUSH</p>
    <h1 class="product-frame">BATH SOAK</h1>
    <p class="tagline-band">The Best Bath Yull Ever Take</p>
    <ul class="benefits">
      <li>For Sore Muscles</li>
      <li>Cooling Vapors</li>
      <li>Smells Good</li>
    </ul>
    <p class="ingredients-pill">Made With<br>Menthol Lemon And Eucalyptus</p>
    <p class="net-weight">Net Weight:<br>15 Ounces (452 grams)</p>
  </section>
</body>
</html>
```